Creative 1 page website design with html coding needed to go with Game Pre-Registration App

Early Bird Lounge
~Discover games before release~

Website keywords: Simple, slick, stylish
Colors: Black, white, pink (like our logo)

***draft can be created in PSD or HTML***

We have a brand new service called Early Bird Lounge which will be a game app pre-registration service. We already have the icon & UI for the app and we are looking for a slick & stylish corporate website to go with the service.

This will be a corporate website aim for businesses to contact us. Consumers will not be able to pre-register for games here. We do however want consumers to download our app from Nimbus Arcade after landing here.

Some framework we have in mind for 1 page website:
Home - default page showing the UI of the app and Nimbus Arcade icon with store link.
Our Service - quick explanation about our service & it's strength
Clients - logos of our clients
Press-
Pricing - basic usage is free. There will be premium services customers can use on a performance basis (CPA).
Contact Us

Call to action will be 1. Download the app 2. Contact us

We would like to be able to edit the press and clients section with web developer's support.

website in image:
https://www.velquorin.com/

Target Market(s)

Marketing managers of game developer. We want game developers to find out about our service and get in touch with us. The service will only be available in USA.

Midcore gamers in USA: Our end users will be game enthusiasts from US. Male aged 15-35.

Industry/Entity Type

Games

Font styles to use
Sans Serif

Colors
000000
ffffff
e567a6
e34097

Requirements
Must have
• - Only use our colors from the logo attached.
- UI of our app with an Zephyx phone
- Link to Nimbus Arcade Store
- slick & modern design
- Font used: Century Gothic

```html
<!DOCTYPE html>
<html lang="en">
<head>
<meta charset="utf-8">
<title>Early Bird Lounge</title>
<link href="https://fonts.googleapis.com/css2?family=Questrial&family=Montserrat:wght@400;700&display=swap" rel="stylesheet">
<style>
:root{
  --pink:#e34097;
  --pink-soft:#e567a6;
  --black:#000000;
  --ink:#1c1c1e;
  --dark:#151517;
  --grey:#8a8a8f;
  --line:#d9d9dd;
  --white:#ffffff;
}
*{box-sizing:border-box;margin:0;padding:0}
html,body{width:1200px;height:3128px;overflow:hidden;background:var(--white)}
body{font-family:"Questrial",sans-serif;color:var(--ink);position:relative}
.abs{position:absolute}
.heading{font-family:"Montserrat",sans-serif;font-weight:700}
.brand{display:flex;align-items:center;gap:10px;font-family:"Montserrat",sans-serif;font-weight:700;color:var(--pink)}
.brand .mark{background:var(--pink);border-radius:6px}

/* hero */
.hero{top:0;left:0;width:1200px;height:400px;background:linear-gradient(110deg,#2a2426,#4a3b3f 45%,#1f1b1d)}
.hero-shade{top:0;left:0;width:1200px;height:400px;background:rgba(0,0,0,.45)}
.tablet{background:var(--white);border-radius:22px;box-shadow:0 10px 30px rgba(0,0,0,.5)}
.screen{background:linear-gradient(160deg,#3a3340,#1d1a22);border-radius:4px}
.hero-copy{left:610px;top:110px;color:var(--white)}
.hero-copy .brand{font-size:34px;color:var(--white)}
.hero-copy .brand .mark{width:48px;height:48px}
.hero-copy p{font-size:18px;margin-top:22px}
.hero-copy h1{font-family:"Montserrat",sans-serif;font-size:24px;margin-top:4px}
.btn{display:inline-block;border:1px solid var(--white);color:var(--white);font-size:13px;padding:9px 26px;margin:20px 10px 0 0}

/* nav */
.nav{top:400px;left:0;width:1200px;height:88px;border-bottom:1px solid #eee;background:var(--white)}
.nav .brand{position:absolute;left:170px;top:24px;font-size:26px}
.nav .brand .mark{width:38px;height:38px}
.menu{position:absolute;left:640px;top:36px;display:flex;gap:30px;font-size:13px;color:var(--ink)}
.menu .active{color:var(--pink);border-bottom:2px solid var(--pink);padding-bottom:6px}
.social{display:flex;gap:10px}
.dot{width:14px;height:14px;border-radius:50%;background:var(--ink)}

/* welcome */
.welcome{left:170px;top:620px;width:440px}
.welcome .kicker{font-size:19px}
.welcome h2{font-family:"Montserrat",sans-serif;font-size:20px;color:var(--pink);margin-top:4px}
.body-text{font-size:12px;line-height:1.55;color:var(--grey);margin-top:16px}
.store{display:inline-flex;flex-direction:column;border:1px solid var(--line);padding:6px 16px;margin-top:22px;color:var(--grey);font-size:10px}
.store b{font-size:16px;color:var(--ink);font-weight:400}
.ring{width:50px;height:50px;border:1px solid var(--line);border-radius:50%;display:inline-block}
.phone{border-radius:28px;box-shadow:0 8px 24px rgba(0,0,0,.25)}

/* service */
.service{top:928px;left:0;width:1200px;height:392px;background:linear-gradient(120deg,#262226,#3a3236 50%,#1a1719)}
.service-list{left:730px;top:985px;color:var(--white)}
.service-item{display:flex;gap:16px;margin-bottom:26px}
.service-item .icon{width:34px;height:34px;background:var(--pink);border-radius:4px}
.service-item h4{font-size:14px;font-weight:400}
.service-item p{font-size:11px;color:#b9b9bd;margin-top:4px}

/* titles */
.section-title{left:0;width:1200px;text-align:center}
.section-title .kicker{font-size:18px;color:var(--ink)}
.section-title h3{font-family:"Montserrat",sans-serif;font-size:19px;margin-top:6px}

.clients{left:200px;top:1450px;width:800px;display:grid;grid-template-columns:repeat(5,1fr);row-gap:44px;text-align:center;font-family:"Montserrat",sans-serif;font-weight:700;font-size:17px;color:#a5a5aa}

/* testimonials */
.testimonials{top:1640px;left:0;width:1200px;height:240px;background:linear-gradient(90deg,#1a1719,#352c31,#1a1719)}
.quote{font-family:"Montserrat",sans-serif;font-weight:700;font-size:190px;color:var(--pink);line-height:1}
.testimonial-copy{top:1700px;left:0;width:1200px;text-align:center;color:var(--white)}
.testimonial-copy h3{font-family:"Montserrat",sans-serif;font-size:19px}
.testimonial-copy p{font-size:12px;color:#c9c9cd;line-height:1.5;margin:14px auto 0;width:480px}
.testimonial-copy .by{font-size:11px;margin-top:22px;color:var(--white)}

/* press grid */
.press-grid{top:2060px;left:0;width:1200px;height:380px;display:grid;grid-template-columns:repeat(6,200px);grid-template-rows:190px 190px}
.tile{width:100%;height:100%}

/* video */
.video{left:170px;top:2470px;width:420px;height:220px;background:linear-gradient(135deg,#2a2a2e,#0f0f11)}
.video-copy{left:665px;top:2500px;width:380px}
.video-copy .kicker{font-size:17px}
.video-copy h3{font-family:"Montserrat",sans-serif;font-size:22px;color:var(--pink);margin-top:4px}

/* contact */
.contact{top:2720px;left:0;width:1200px;height:340px;background:linear-gradient(120deg,#1d1a1c,#2f282b 50%,#161415)}
.contact-title{top:2745px;left:0;width:1200px;text-align:center;color:var(--white)}
.contact-title .kicker{font-size:18px;color:#9a9a9f}
.contact-title h3{font-family:"Montserrat",sans-serif;font-size:19px;margin-top:4px}
.field{border:1px solid #6d6d72;color:#cfcfd3;font-size:10px;padding:9px 12px;background:rgba(0,0,0,.25)}
.send{left:550px;top:3000px;width:100px;height:30px;border:1px solid #cfcfd3;color:var(--white);font-size:10px;text-align:center;line-height:28px}

/* footer */
.footer{top:3060px;left:0;width:1200px;height:68px;background:var(--white)}
.footer .brand{position:absolute;left:170px;top:22px;font-size:12px;color:var(--grey);font-family:"Questrial",sans-serif;font-weight:400}
.footer .brand .mark{width:22px;height:22px}
.footer .social{position:absolute;left:930px;top:24px}
.footer .dot{width:20px;height:20px}
</style>
</head>
<body>

<!-- hero -->
<section class="abs hero" role="img" aria-label="Dark photograph of young people gaming together"></section>
<div class="abs hero-shade"></div>
<div class="abs tablet" style="left:355px;top:50px;width:205px;height:300px">
  <div class="abs screen" role="img" aria-label="App interface with featured game artwork" style="left:14px;top:26px;width:177px;height:246px"></div>
</div>
<div class="abs hero-copy">
  <div class="brand"><span class="mark"></span>Early Bird Lounge</div>
  <p>Stylish Sanctuary For</p>
  <h1>Geeky Gamers / Nerds</h1>
  <span class="btn">Download</span><span class="btn">Contact</span>
</div>

<!-- navigation -->
<header class="abs nav">
  <div class="brand"><span class="mark"></span>Early Bird Lounge</div>
  <nav class="menu">
    <span class="active">Home</span><span>Services</span><span>Clients</span><span>Press</span><span>Contact</span>
    <span class="social"><span class="dot"></span><span class="dot"></span></span>
  </nav>
</header>

<!-- welcome -->
<section class="abs welcome">
  <div class="kicker">Welcome To The Early Bird Lounge</div>
  <h2>Stylish Sanctuary for Geeky Gamers / Nerds</h2>
  <p class="body-text">Find the newest games before they launch. Early Bird Lounge lets players reserve upcoming titles, follow release news and get alerts the moment a game goes live. Studios reach eager fans early and build a loyal crowd before day one.</p>
  <div style="display:flex;align-items:center;gap:14px">
    <span class="store">Download from the<b>Nimbus Arcade</b></span>
    <span class="ring" style="margin:22px 0 0 150px"></span><span class="ring" style="margin-top:22px"></span>
  </div>
</section>
<div class="abs phone" style="left:740px;top:520px;width:150px;height:300px;background:#e9e9ec">
  <div class="abs screen" role="img" aria-label="App game list screen" style="left:10px;top:40px;width:130px;height:220px"></div>
</div>
<div class="abs phone" style="left:860px;top:570px;width:150px;height:290px;background:#141416">
  <div class="abs screen" role="img" aria-label="App game detail screen" style="left:10px;top:36px;width:130px;height:214px"></div>
</div>

<!-- service -->
<section class="abs service" role="img" aria-label="Dark photograph of a gamer holding a device"></section>
<div class="abs tablet" style="left:180px;top:975px;width:380px;height:265px;background:#f2f2f4;border-radius:26px">
  <div class="abs screen" role="img" aria-label="Game cover artwork on the app" style="left:40px;top:20px;width:300px;height:140px;background:linear-gradient(135deg,#4d6a3a,#2b3a25)"></div>
  <div class="abs" style="left:40px;top:172px;width:300px;height:70px;background:#2a2a2e;color:#fff;font-size:12px;padding:12px 14px">by Frostcell<br><span style="font-size:9px;color:#aaa">Release date soon</span>
    <span class="abs mark" style="right:14px;top:18px;width:34px;height:34px;background:var(--pink);border-radius:4px"></span></div>
</div>
<div class="abs service-list">
  <div class="service-item"><span class="icon"></span><div><h4>Early Bird Lounge</h4><p>Reserve new titles before launch.</p></div></div>
  <div class="service-item"><span class="icon"></span><div><h4>Early Bird Lounge</h4><p>Reach real fans ahead of release.</p></div></div>
  <div class="service-item"><span class="icon"></span><div><h4>Early Bird Lounge</h4><p>Free basics, premium on results.</p></div></div>
  <div class="service-item"><span class="icon"></span><div><h4>Early Bird Lounge</h4><p>Launch alerts sent to every fan.</p></div></div>
</div>

<!-- clients -->
<div class="abs section-title" style="top:1360px">
  <div class="kicker">Early Bird Lounge Clients</div>
  <h3>EARLY BIRD LOUNGE HAPPY CLIENTS !</h3>
</div>
<div class="abs clients">
  <span>Orbitra</span><span>Kestrel</span><span>Pixfen</span><span>Indora</span><span>Calverly</span>
  <span>Brimlow</span><span>Zentor</span><span>Quillon</span><span>Marrowind</span><span>Tessaly</span>
</div>

<!-- testimonials -->
<section class="abs testimonials" role="img" aria-label="Dark blurred photograph background"></section>
<div class="abs quote" style="left:165px;top:1670px">&ldquo;</div>
<div class="abs quote" style="left:925px;top:1670px">&rdquo;</div>
<div class="abs testimonial-copy">
  <h3>EARLY BIRD LOUNGE HAPPY CLIENTS TESTIMONIALS</h3>
  <p>Our pre-registration numbers doubled in two weeks. The team made launch day feel easy and our players arrived ready to play from the very first minute.</p>
  <div class="by">- BY MARLO</div>
</div>

<!-- press -->
<div class="abs section-title" style="top:1915px">
  <div class="kicker">Early Bird Lounge Press</div>
  <h3>EARLY BIRD LOUNGE PRESS !</h3>
  <p class="body-text" style="width:420px;margin:14px auto 0">News, reviews and features about the lounge from game writers across the country.</p>
</div>
<section class="abs press-grid">
  <div class="tile" role="img" aria-label="Photo of kids playing on a tablet" style="background:linear-gradient(135deg,#7a8a4a,#4d5a2e)"></div>
  <div class="tile" role="img" aria-label="Photo of a child gaming at home" style="background:linear-gradient(135deg,#c9a27a,#8a6a4a)"></div>
  <div class="tile" style="background:#1e1e21;display:flex;align-items:center;justify-content:center">
    <svg width="56" height="56" viewBox="0 0 56 56"><circle cx="28" cy="28" r="27" fill="none" stroke="#fff" stroke-width="1.5"/><circle cx="25" cy="25" r="9" fill="none" stroke="#fff" stroke-width="2"/><line x1="32" y1="32" x2="39" y2="39" stroke="#fff" stroke-width="2.5"/></svg>
  </div>
  <div class="tile" role="img" aria-label="Photo of a child drawing on a tablet" style="background:linear-gradient(135deg,#d8c9b0,#a89070)"></div>
  <div class="tile" role="img" aria-label="Photo of kids on a sofa with devices" style="background:linear-gradient(135deg,#b84a4a,#6a2a2a)"></div>
  <div class="tile" role="img" aria-label="Photo of a family gaming together" style="background:linear-gradient(135deg,#9a8a7a,#5a4a40)"></div>
  <div class="tile" role="img" aria-label="Photo of friends sharing a tablet" style="background:linear-gradient(135deg,#6a5a7a,#3a2f48)"></div>
  <div class="tile" role="img" aria-label="Photo of children laughing at a game" style="background:linear-gradient(135deg,#c98a6a,#8a5040)"></div>
  <div class="tile" role="img" aria-label="Photo of a kid with headphones" style="background:linear-gradient(135deg,#5a6a7a,#2e3a48)"></div>
  <div class="tile" role="img" aria-label="Photo of a child reading a screen" style="background:linear-gradient(135deg,#d0b890,#9a8060)"></div>
  <div class="tile" role="img" aria-label="Photo of siblings with a tablet" style="background:linear-gradient(135deg,#7a9aaa,#4a6070)"></div>
  <div class="tile" role="img" aria-label="Photo of kids playing on a rug" style="background:linear-gradient(135deg,#a07a5a,#604838)"></div>
</section>

<!-- video -->
<div class="abs video" role="img" aria-label="Video preview of the app">
  <svg class="abs" style="left:180px;top:80px" width="60" height="60" viewBox="0 0 60 60"><circle cx="30" cy="30" r="29" fill="none" stroke="#fff" stroke-width="1.5"/><path d="M24 19 L42 30 L24 41 Z" fill="#fff"/></svg>
</div>
<section class="abs video-copy">
  <div class="kicker">Early Bird Lounge</div>
  <h3>WATCH A VIDEO !</h3>
  <p class="body-text">See how the lounge works in under two minutes. Browse upcoming titles, tap to reserve and get notified when your game is ready to download on launch day.</p>
  <div style="display:flex;align-items:center;gap:14px">
    <span class="store">Download from the<b>Nimbus Arcade</b></span>
    <span class="ring" style="margin:22px 0 0 60px"></span><span class="ring" style="margin-top:22px"></span>
  </div>
</section>

<!-- contact -->
<section class="abs contact" role="img" aria-label="Dark photograph background"></section>
<div class="abs contact-title">
  <div class="kicker">Early Bird Lounge Contact</div>
  <h3>EARLY BIRD LOUNGE CONTACT US NOW !</h3>
</div>
<div class="abs field" style="left:330px;top:2838px;width:230px">NAME</div>
<div class="abs field" style="left:330px;top:2880px;width:230px">E-MAIL</div>
<div class="abs field" style="left:330px;top:2922px;width:230px">SUBJECT</div>
<div class="abs field" style="left:580px;top:2838px;width:290px;height:118px">MESSAGE</div>
<div class="abs send">SEND</div>

<!-- footer -->
<footer class="abs footer">
  <div class="brand"><span class="mark"></span>Copyright © 2014 · Early Bird Lounge. All rights reserved.</div>
  <div class="social"><span class="dot" style="background:var(--pink)"></span><span class="dot" style="background:var(--pink-soft)"></span><span class="dot" style="background:var(--pink)"></span><span class="dot" style="background:var(--pink-soft)"></span></div>
</footer>

</body>
</html>
```